SkyRavelin Unique Gift Certificate

We need a unique, luxury gift certificate created for our online company (SkyRavelin). We are looking for something out of the ordinary, ie. do not want it to look like a 'normal' gift certificate. Please visit our website to gain a feel for our company (skyravelin.com.au). The dimensions are 148x148mm. We need our logo, website details, to, from, description, code, exp date included. The certificate will be printed on wood veneer so watermarks will not work. We want it to be clean and minimalistic.

Industry/Entity Type

It Company

```html
<!DOCTYPE html>
<html lang="en">
<head>
<meta charset="utf-8">
<title>SkyRavelin Gift Certificate</title>
<link rel="stylesheet" href="https://fonts.googleapis.com/css2?family=Rye&family=Old+Standard+TT:wght@400&display=swap">
<style>
  :root {
    --wood-light: #c7662a;
    --wood-mid: #b4561f;
    --wood-dark: #93401a;
    --ink: #3b1d0e;
    --accent-fill: rgba(59, 29, 14, 0.45);
  }
  * { margin: 0; padding: 0; box-sizing: border-box; }
  html, body { width: 1200px; height: 1200px; overflow: hidden; background: var(--wood-mid); }
  .certificate {
    position: relative;
    width: 1200px;
    height: 1200px;
    font-family: "Old Standard TT", "Times New Roman", serif;
    color: var(--ink);
  }
  .wood-surface {
    position: absolute;
    inset: 0;
    background:
      radial-gradient(ellipse at 30% 20%, rgba(220,130,60,0.35), transparent 60%),
      radial-gradient(ellipse at 70% 80%, rgba(120,50,15,0.3), transparent 60%),
      linear-gradient(160deg, var(--wood-light), var(--wood-mid) 50%, var(--wood-dark));
  }
  .frame {
    position: absolute;
    left: 55px;
    top: 43px;
    width: 1090px;
    height: 1113px;
    border: 6px solid var(--ink);
    border-radius: 10px;
  }
  .brand {
    position: absolute;
    top: 110px;
    left: 0;
    width: 1200px;
    text-align: center;
  }
  .brand-circle {
    display: block;
    margin: 0 auto;
    width: 148px;
    height: 148px;
    border: 6px solid var(--ink);
    border-radius: 50%;
  }
  .brand-name {
    display: block;
    margin-top: 4px;
    font-size: 24px;
    letter-spacing: 1px;
  }
  .title {
    position: absolute;
    top: 360px;
    left: 0;
    width: 1200px;
    text-align: center;
    font-family: "Rye", serif;
    font-size: 84px;
    font-weight: 400;
    letter-spacing: 2px;
  }
  .fields {
    position: absolute;
    top: 547px;
    left: 212px;
    width: 784px;
    list-style: none;
  }
  .field {
    display: flex;
    align-items: baseline;
    height: 91px;
    font-size: 46px;
  }
  .field-label { white-space: pre; margin-right: 22px; }
  .field-line {
    flex: 1;
    border-bottom: 3px solid var(--ink);
    height: 34px;
  }
  .footer {
    position: absolute;
    top: 1066px;
    left: 143px;
    width: 914px;
    display: flex;
    align-items: center;
    justify-content: space-between;
  }
  .accent-band {
    width: 238px;
    height: 28px;
    background: var(--accent-fill);
  }
  .website { font-size: 32px; }
</style>
</head>
<body>
<main class="certificate">
  <div class="wood-surface" role="img" aria-label="Warm orange-brown wood veneer grain"></div>
  <div class="frame"></div>

  <header class="brand">
    <span class="brand-circle"></span>
    <span class="brand-name">SkyRavelin</span>
  </header>

  <h1 class="title">GIFT CERTIFICATE</h1>

  <ul class="fields">
    <li class="field"><span class="field-label">To :</span><span class="field-line"></span></li>
    <li class="field"><span class="field-label">From :</span><span class="field-line"></span></li>
    <li class="field"><span class="field-label">Description:</span><span class="field-line"></span></li>
    <li class="field"><span class="field-label">Code :</span><span class="field-line"></span></li>
    <li class="field"><span class="field-label">Valid till :</span><span class="field-line"></span></li>
  </ul>

  <footer class="footer">
    <div class="accent-band" role="img" aria-label="Decorative flourish area"></div>
    <span class="website">www.skyravelin.com.au</span>
    <div class="accent-band" role="img" aria-label="Decorative flourish area"></div>
  </footer>
</main>
</body>
</html>
```